Granite Ridge Holdings

I have a real estate investment business.

** I need editable vector files of the final design.

Industry/Entity Type

Real Estate

Contact Information for Business Card

I would like the card to be clear and direct with the company name and contact info. I would prefer not to have a design that is too busy (i.e., with excessive detail) in the business card.

Font styles to use
Sans Serif

Requirements
Must have
• My card must have the following information listed below:
• Company name: Grainite Ridge Holdings LLC
• My name: Daniel Vorsley
• Phone number: (555) 218-9067
• Email address: dtvorsley@mailbox-example.net
• Keywords: “Real Estate Investments”
Nice to have
• I would like to have a design that resembles the characteristics/uses of obsidian stone which resembles something related to strength and resilience. Perhaps something with sharp, sleek color transitions as well.

```html
<!DOCTYPE html>
<html lang="en">
<head>
<meta charset="utf-8">
<title>Grainite Ridge Holdings LLC – Business Card</title>
<link rel="stylesheet" href="https://fonts.googleapis.com/css2?family=Oswald:wght@600&family=Work+Sans:wght@400;500&display=swap">
<style>
  :root {
    --page-bg: #151515;
    --card-bg: #232323;
    --card-edge: #2c2c2c;
    --ink: #f4f4f4;
    --ink-soft: #d8d8d8;
  }
  * { margin: 0; padding: 0; box-sizing: border-box; }
  html, body {
    width: 1200px; height: 900px; overflow: hidden;
    background: var(--page-bg);
    font-family: "Work Sans", Arial, sans-serif;
    color: var(--ink);
  }
  .sheet {
    width: 1200px; height: 900px;
    display: flex; flex-direction: column; align-items: center; justify-content: center;
    gap: 36px;
  }
  .card {
    position: relative;
    width: 660px; height: 377px;
    background: linear-gradient(135deg, var(--card-bg) 0%, #1e1e1e 55%, #2a2a2a 100%);
    border: 1px solid var(--card-edge);
  }
  /* Front */
  .card-front {
    display: flex; flex-direction: column; align-items: center; justify-content: center;
  }
  .wordmark {
    font-size: 34px; font-weight: 500; letter-spacing: 3px;
    text-transform: uppercase; text-align: center; line-height: 1.25;
    color: var(--ink);
  }
  .tagline {
    margin-top: 48px;
    font-size: 17px; letter-spacing: 1.2px; color: var(--ink-soft);
  }
  /* Back */
  .identity {
    position: absolute; top: 128px; right: 362px; text-align: right;
  }
  .person-name {
    font-family: "Oswald", "Arial Narrow", sans-serif;
    font-weight: 600; font-size: 36px; letter-spacing: 1px;
    text-transform: uppercase; line-height: 1.1;
  }
  .person-title { font-size: 17px; margin-top: 6px; letter-spacing: .5px; }
  .divider {
    position: absolute; left: 322px; top: 132px;
    width: 2px; height: 70px; background: var(--ink);
  }
  .contact-list {
    position: absolute; left: 346px; top: 126px; list-style: none;
    font-size: 16px; line-height: 27px; letter-spacing: .4px;
  }
  .contact-list li { display: flex; align-items: center; gap: 10px; white-space: nowrap; }
  .contact-list svg { width: 13px; height: 13px; flex: none; }
  .address {
    position: absolute; left: 0; right: 0; bottom: 58px;
    text-align: center; font-size: 18px; letter-spacing: .6px;
  }
</style>
</head>
<body>
<main class="sheet">
  <section class="card card-front" aria-label="Card front">
    <h1 class="wordmark">Grainite Ridge<br>Holdings LLC</h1>
    <p class="tagline">Real Estate Investments</p>
  </section>

  <section class="card card-back" aria-label="Card back">
    <div class="identity">
      <p class="person-name">Daniel Vorsley</p>
      <p class="person-title">Director</p>
    </div>
    <span class="divider"></span>
    <ul class="contact-list">
      <li>
        <svg viewBox="0 0 24 24" aria-hidden="true"><path d="M6.6 10.8a15 15 0 0 0 6.6 6.6l2.2-2.2c.3-.3.7-.4 1-.2 1.1.4 2.3.6 3.6.6.6 0 1 .4 1 1V20c0 .6-.4 1-1 1A17 17 0 0 1 3 4c0-.6.4-1 1-1h3.5c.6 0 1 .4 1 1 0 1.3.2 2.5.6 3.6.1.3 0 .7-.2 1z" fill="#f4f4f4"/></svg>
        (555) 218-9067
      </li>
      <li>
        <svg viewBox="0 0 24 24" aria-hidden="true"><rect x="3" y="5" width="18" height="14" fill="none" stroke="#f4f4f4" stroke-width="2"/><path d="M3 6l9 7 9-7" fill="none" stroke="#f4f4f4" stroke-width="2"/></svg>
        dtvorsley@mailbox-example.net
      </li>
      <li>
        <svg viewBox="0 0 24 24" aria-hidden="true"><circle cx="12" cy="12" r="9" fill="none" stroke="#f4f4f4" stroke-width="2"/><path d="M3 12h18M12 3c3 3 3 15 0 18M12 3c-3 3-3 15 0 18" fill="none" stroke="#f4f4f4" stroke-width="1.6"/></svg>
        grainiteridge-example.com
      </li>
    </ul>
    <p class="address">2271 Larkfield Mill Road Marston, NE 68014</p>
  </section>
</main>
</body>
</html>
```